A small boutique Accounting and Mortgage Broking firm needs a business card design

Quorvel is a Brisbane based boutique accounting and mortgage broking firm. We offer a range of extensive financial services like accounting, tax consulting, book-keeping and mortgage broking.
We need a business card that stands out. The content can stay as it is on the existing card unless you recommend us to change anything on it for a better design.
Please remove the mobile number and give us a suitable format to change the details like email address and name.
Industry/Entity Type
Business
Contact Information for Business Card
Dalian Okoruwe
Quorvel Group Pty Ltd
3/412 Brackwin Rd Salisbury QLD 4107
PO Box 829 Salisbury QLD 4107
T 07 3184 5526
F 07 3952 1087
E dokoruwe@quorvel.net.au
Accountants Tax Agents, Mortgage Brokers
www.quorvel.net.au
Look and feel
Each slider illustrates characteristics of the customer's brand and the style your logo design should communicate.

```html
<!DOCTYPE html>
<html lang="en">
<head>
<meta charset="utf-8">
<title>Quorvel Business Card</title>
<link rel="stylesheet" href="https://fonts.googleapis.com/css2?family=Open+Sans:wght@400;600;700;800&display=swap">
<style>
  :root {
    --bg: #e9e6e1;
    --card: #f4f4f4;
    --ink: #1b1b1b;
    --watermark: #c9c9c9;
    --dark: #3d3d3d;
    --darker: #2a2a2a;
    --green: #6cc62e;
    --green-dark: #55a81f;
    --light-text: #e8e8e8;
  }
  * { margin: 0; padding: 0; box-sizing: border-box; }
  html, body { width: 1200px; height: 900px; overflow: hidden; }
  body {
    background: var(--bg);
    font-family: "Open Sans", Arial, sans-serif;
    position: relative;
  }
  .card {
    position: absolute;
    left: 260px;
    width: 680px;
    height: 390px;
    background: linear-gradient(160deg, #ffffff 0%, var(--card) 60%, #e6e6e6 100%);
    overflow: hidden;
    box-shadow: 0 8px 24px rgba(0,0,0,0.18);
  }
  .card--front { top: 40px; }
  .card--back { top: 470px; }
  .card svg.shapes { position: absolute; inset: 0; }

  .front__brand-mark {
    position: absolute;
    left: 0; right: 0; top: 78px;
    text-align: center;
    font-weight: 800;
    font-size: 120px;
    letter-spacing: -2px;
    color: var(--watermark);
    opacity: 0.45;
  }
  .front__tagline {
    position: absolute;
    left: 48px; top: 142px;
    font-weight: 800;
    font-size: 44px;
    letter-spacing: 0.5px;
    color: var(--ink);
  }

  .back__person { position: absolute; left: 128px; top: 100px; color: var(--ink); }
  .back__name { font-size: 26px; font-weight: 400; }
  .back__title { font-size: 15px; font-weight: 600; letter-spacing: 1.5px; margin: 6px 0 0 50px; }

  .back__brand {
    position: absolute; left: 42px; top: 190px;
    display: flex; align-items: center; gap: 18px;
  }
  .back__brand-dot {
    width: 76px; height: 76px; border-radius: 50%;
    background: var(--darker);
  }
  .back__brand-name {
    font-size: 58px; font-weight: 800; color: var(--green); letter-spacing: -1px;
  }

  .contact {
    position: absolute; right: 0;
    height: 34px;
    display: flex;
  }
  .contact__text {
    display: flex; align-items: center;
    padding: 0 22px;
    font-size: 15px;
    color: var(--light-text);
    background: var(--dark);
  }
  .contact__icon {
    width: 44px;
    display: flex; align-items: center; justify-content: center;
    background: var(--darker);
    color: #fff; font-weight: 700; font-size: 20px;
  }
  .contact--phone { top: 38px; }
  .contact--address { top: 88px; }
  .contact--address .contact__text { background: var(--green); color: #fff; font-weight: 600; padding: 0 30px; }
  .contact--address .contact__icon { background: var(--green-dark); }
  .contact--email { top: 138px; }

  .back__web {
    position: absolute; left: 0; right: 0; bottom: 14px;
    text-align: center;
    font-size: 20px; letter-spacing: 1px;
    color: var(--light-text);
  }
</style>
</head>
<body>

  <section class="card card--front">
    <p class="front__brand-mark" aria-hidden="true">Quorvel</p>
    <svg class="shapes" width="680" height="390" viewBox="0 0 680 390">
      <path d="M380,258 C470,240 580,222 680,206 L680,214 C580,226 480,244 380,258 Z" fill="var(--darker)"/>
      <path d="M0,330 C220,318 460,270 680,226 L680,240 C470,296 240,350 0,378 Z" fill="var(--green)"/>
    </svg>
    <h1 class="front__tagline">TRUST.VALUE.GROWTH</h1>
  </section>

  <section class="card card--back">
    <svg class="shapes" width="680" height="390" viewBox="0 0 680 390">
      <path d="M0,390 L0,322 C220,340 480,290 680,176 L680,390 Z" fill="var(--dark)"/>
      <path d="M0,300 C200,318 430,300 580,262 C430,316 220,336 0,322 Z" fill="var(--green)"/>
    </svg>

    <div class="back__person">
      <p class="back__name">Rowan Pell</p>
      <p class="back__title">Manager</p>
    </div>

    <div class="back__brand">
      <span class="back__brand-dot"></span>
      <span class="back__brand-name">Quorvel</span>
    </div>

    <div class="contact contact--phone">
      <span class="contact__text">90000417</span>
      <span class="contact__icon">
        <svg width="20" height="18" viewBox="0 0 20 18" aria-hidden="true">
          <path d="M2,6 C2,2 18,2 18,6 L15,7.5 L13,5 L7,5 L5,7.5 Z" fill="#fff"/>
          <rect x="4" y="9" width="12" height="7" rx="1.5" fill="none" stroke="#fff" stroke-width="2"/>
        </svg>
      </span>
    </div>
    <div class="contact contact--address">
      <span class="contact__text">Street14 H#208 , Sydney</span>
      <span class="contact__icon">
        <svg width="16" height="20" viewBox="0 0 16 20" aria-hidden="true">
          <path d="M8,1 C4,1 1,4 1,8 C1,13 8,19 8,19 C8,19 15,13 15,8 C15,4 12,1 8,1 Z" fill="#fff"/>
          <circle cx="8" cy="8" r="2.5" fill="var(--green-dark)"/>
        </svg>
      </span>
    </div>
    <div class="contact contact--email">
      <span class="contact__text">ardel@mailbox.com</span>
      <span class="contact__icon">@</span>
    </div>

    <p class="back__web">www.ardel.com.sa</p>
  </section>

</body>
</html>
```